Upgrade/"Tweak" My Landing Page

We need to "tweak" our current landing page. I'm a perfectionist and something seems "off". Things I LOVE about our current page: I love our message that "ONE SIZE DOES NOT FIT ALL", as well as the photo used (boy wearing an oversized hat). I also like the fact that the photo is in full screen mode- I like this look.
THINGS I DON'T Like: The font & location of our message "ONE SIZE DOES NOT FIT ALL" - just seems "off". I'm also concerned about the placement of our menu being on the left hand side of the screen. Not sure if this is ideal. Also, my product types are listed on the left hand side of the screen in the menu section. My audience seems to think these are links when in fact they are just examples of the products I sell. How can I position these so the audience knows it's for informational purposes only.
Help!! I want my landing page to be PERFECT.

```html
<!DOCTYPE html>
<html lang="en">
<head>
<meta charset="utf-8">
<title>Harborline Insurance Agency</title>
<link href="https://fonts.googleapis.com/css2?family=Roboto+Condensed:wght@300;400;700&display=swap" rel="stylesheet">
<style>
  :root {
    --navy: #1d3a63;
    --navy-soft: #2c4f80;
    --white: #ffffff;
    --sky-top: #b9cfe9;
    --sky-mid: #8fb6e6;
    --sky-low: #a6c9ef;
    --hat-red: rgba(232, 86, 96, 0.55);
    --skin: rgba(176, 118, 92, 0.45);
  }
  * { box-sizing: border-box; margin: 0; padding: 0; }
  html, body { width: 1200px; height: 862px; overflow: hidden; }
  body { font-family: "Roboto Condensed", "Arial Narrow", sans-serif; position: relative; }

  .hero-photo {
    position: absolute; inset: 0;
    background:
      radial-gradient(ellipse 480px 210px at 600px 370px, var(--hat-red), transparent 75%),
      radial-gradient(ellipse 360px 380px at 590px 780px, var(--skin), transparent 72%),
      linear-gradient(180deg, var(--sky-top) 0%, var(--sky-mid) 45%, var(--sky-low) 100%);
  }

  .brand {
    position: absolute; left: 105px; top: 44px;
    display: flex; align-items: center; gap: 10px;
    color: var(--navy); font-weight: 700; font-size: 22px; letter-spacing: 0.5px;
  }
  .brand-mark { width: 22px; height: 22px; border-radius: 50%; background: var(--navy-soft); }

  .social { position: absolute; top: 21px; left: 1032px; display: flex; gap: 6px; }
  .social span { width: 29px; height: 29px; background: var(--navy-soft); display: block; }

  .main-nav { position: absolute; top: 70px; left: 0; width: 1200px; font-size: 23px; color: var(--navy); }
  .main-nav a { position: absolute; color: inherit; text-decoration: none; line-height: 22px; white-space: nowrap; }

  .headline {
    position: absolute; top: 292px; left: 0; width: 1200px; text-align: center;
    color: var(--white); font-weight: 700; font-size: 95px; line-height: 100px; letter-spacing: -0.5px;
  }
  .tagline {
    position: absolute; top: 390px; left: 0; width: 1200px; text-align: center;
    color: var(--white); font-weight: 300; font-size: 41px; letter-spacing: 4.2px;
  }

  .products { position: absolute; top: 698px; left: 0; width: 1200px; color: var(--white); text-align: center; }
  .products h2 { font-size: 23px; font-weight: 700; margin-left: -25px; }
  .product-row { display: flex; justify-content: center; gap: 19px; margin-top: 10px; font-size: 20px; }
  .product-row + .product-row { margin-top: 7px; }
  .product { display: flex; align-items: center; gap: 11px; }
  .product svg { width: 31px; height: 31px; }
</style>
</head>
<body>
  <div class="hero-photo" role="img" aria-label="Full-screen photo of a child wearing an oversized red sun hat against a blue sky"></div>

  <div class="brand"><span class="brand-mark"></span>HARBORLINE INSURANCE AGENCY</div>

  <div class="social" aria-label="Social links"><span></span><span></span></div>

  <nav class="main-nav">
    <a style="left:401px">About us</a>
    <a style="left:514px">Pay your bill</a>
    <a style="left:659px">Request a quote or<br>policy change</a>
    <a style="left:865px">File a claim</a>
    <a style="left:1002px">Contact us</a>
  </nav>

  <h1 class="headline">ONE SIZE DOES NOT FIT ALL</h1>
  <p class="tagline">Custom-made solutions at your fingertips</p>

  <section class="products">
    <h2>OUR INSURANCE PRODUCTS</h2>
    <div class="product-row">
      <div class="product"><svg viewBox="0 0 32 32"><circle cx="16" cy="16" r="16" fill="#fff"/><path d="M9 16 16 9l7 7h-2v7h-4v-4h-2v4h-4v-7z" fill="#1d3a63"/></svg>Home</div>
      <div class="product"><svg viewBox="0 0 32 32"><circle cx="16" cy="16" r="16" fill="#fff"/><rect x="11" y="9" width="10" height="14" fill="none" stroke="#1d3a63" stroke-width="2"/><path d="M11 14h10M11 18h10M16 9v14" stroke="#1d3a63" stroke-width="1.5"/></svg>Condo</div>
      <div class="product"><svg viewBox="0 0 32 32"><circle cx="16" cy="16" r="16" fill="#fff"/><path d="M9 10h14M10 14h12M12 18h8M14 22h4" stroke="#1d3a63" stroke-width="2" stroke-linecap="round"/></svg>Windstorm</div>
      <div class="product"><svg viewBox="0 0 32 32"><circle cx="16" cy="16" r="16" fill="#fff"/><path d="M10 17 16 11l6 6v4H10z" fill="#1d3a63"/><path d="M8 23q2-2 4 0t4 0 4 0 4 0" stroke="#1d3a63" stroke-width="1.8" fill="none"/></svg>Flood</div>
      <div class="product"><svg viewBox="0 0 32 32"><circle cx="16" cy="16" r="16" fill="#fff"/><path d="M9 19v-3l2-4h10l2 4v3z" fill="#1d3a63"/><circle cx="12" cy="20" r="1.8" fill="#1d3a63"/><circle cx="20" cy="20" r="1.8" fill="#1d3a63"/></svg>Car</div>
    </div>
    <div class="product-row">
      <div class="product"><svg viewBox="0 0 32 32"><circle cx="16" cy="16" r="16" fill="#fff"/><rect x="9" y="12" width="14" height="10" fill="#1d3a63"/><rect x="13" y="9" width="6" height="3" fill="none" stroke="#1d3a63" stroke-width="1.5"/></svg>Business</div>
      <div class="product"><svg viewBox="0 0 32 32"><circle cx="16" cy="16" r="16" fill="#fff"/><path d="M16 8v11h-6zM17 10l5 9h-5z" fill="#1d3a63"/><path d="M9 21h14l-2 3H11z" fill="#1d3a63"/></svg>Boat</div>
      <div class="product"><svg viewBox="0 0 32 32"><circle cx="16" cy="16" r="16" fill="#fff"/><circle cx="10" cy="20" r="3" fill="none" stroke="#1d3a63" stroke-width="1.8"/><circle cx="22" cy="20" r="3" fill="none" stroke="#1d3a63" stroke-width="1.8"/><path d="M10 20l4-5h5l3 5M18 15l1-3h2" stroke="#1d3a63" stroke-width="1.8" fill="none"/></svg>Motorcycle</div>
      <div class="product"><svg viewBox="0 0 32 32"><circle cx="16" cy="16" r="16" fill="#fff"/><path d="M9 14a8 8 0 0 1 12-4z" fill="none" stroke="#1d3a63" stroke-width="1.5"/><path d="M15 12l5 9q1 2-1 2" stroke="#1d3a63" stroke-width="1.5" fill="none"/></svg>Personal umbrella policy</div>
    </div>
  </section>
</body>
</html>
```